Website for a company offering full serivce charging solutions for electric cars

The company "mero-kant" (english: "mero-edge") offering all-in-one-solutions for charging infrastructure for electric mobility.

There are four products:
1- Wallboxes for single-family homes
2- Solutions for property devloper/-management for property parking space
3- All-in-one-charging solution for municipalities/communities
4- Solutions for tourism/hotels/holiday appartments

The Website structure:
1. Main Page
2.1. Product Page Single Homes
2.2. Product Page Property Management / Parking
2.3. Product Page Municipality
2.4. Product Page Tourism
3. Contact Form / Request for information
4. Imprint / Legal

The Website should be built on Wordpress with a powerful possibility to simply add/modify specific landing pages.

We would like you to implement the website later and also maintain it if possible, but we would be able to do minor modifications by ourselfs (for A/B-Testing)

The website should be clear and simple, easy to understand.
Target group is mainly B2C without deeper knowledge of that topic.

It should suggest, that we will provide a very simple way to get the charging infrastructure done.

We need a contact form, maybe we will use Hubspot later.

Attached you will find a draft of the main page and a landing page (for 2.2) - it is just the content, please ignore the design. We would love to let you create a suitable design.
Also you will find some drafts a bit different for the same story.

I added also a few stock photos, but they don't need to be used! If you have better ideas, you are welcome!

Industry/Entity Type

Charging/Electric mobility

Number of Pages Required

2 page

Font styles to use
Sans Serif

Requirements
Must have
• Based on Wordpress, and the designer should be able to implement it on Wordpress on a later step

```html
<!DOCTYPE html>
<html lang="en">
<head>
<meta charset="utf-8">
<title>mero-kant.de – Charging solutions</title>
<link rel="stylesheet" href="https://fonts.googleapis.com/css2?family=Saira:wght@500;600;700;800&family=Montserrat:ital,wght@0,400;0,500;0,600;1,600&display=swap">
<style>
  :root{
    --page:#061629;
    --panel:#0a2140;
    --field:#13325a;
    --ghost:#0d2a48;
    --ghost2:#12304f;
    --white:#ffffff;
    --line:#8b9ab0;
    --pink:#e3128f;
    --violet:#8b55c9;
    --tick:#7b5fd8;
    --text-dark:#0b1a2c;
  }
  *{box-sizing:border-box;margin:0;padding:0}
  html,body{width:1200px;height:2595px;overflow:hidden}
  body{background:var(--page);color:var(--white);font-family:"Montserrat",sans-serif;position:relative}
  .abs{position:absolute}

  /* hero */
  .hero{position:absolute;left:0;top:0;width:1200px;height:750px;
    background:
      radial-gradient(ellipse 420px 520px at 760px 330px, rgba(201,120,40,.75), transparent 70%),
      radial-gradient(ellipse 380px 420px at 1050px 420px, rgba(60,80,230,.55), transparent 70%),
      linear-gradient(180deg,#0e2138 0%,#3a4a6e 30%,#6a5a6a 48%,#20304e 70%,#0c1a30 100%);}
  .hero::after{content:"";position:absolute;inset:0;
    background:linear-gradient(90deg,rgba(8,22,42,.85) 0%,rgba(8,22,42,.55) 40%,rgba(8,22,42,0) 60%);}
  .hero-edge{position:absolute;left:0;top:700px;width:1200px;height:110px}

  .brand{left:112px;top:48px;display:flex;align-items:center;gap:10px;
    font-family:"Saira",sans-serif;font-weight:600;font-size:34px;color:var(--white);z-index:2}
  .brand-dot{width:22px;height:22px;border-radius:50%;background:var(--pink)}
  .nav{right:112px;top:60px;display:flex;gap:33px;z-index:2;
    font-family:"Saira",sans-serif;font-weight:600;font-size:18px}

  .hero-copy{left:112px;top:134px;width:510px;z-index:2}
  .kicker{font-family:"Montserrat",sans-serif;font-style:italic;font-weight:600;font-size:26px;color:var(--pink);line-height:34px}
  .hero-title{font-family:"Saira",sans-serif;font-weight:700;font-size:42px;line-height:52px;margin-top:8px;letter-spacing:.5px}
  .hero-copy p{font-size:17px;line-height:25px;margin-top:24px}
  .hero-copy .lead{margin-top:20px}

  /* section heading */
  .sec-head{left:0;width:1200px;text-align:center}
  .ghost{font-family:"Saira",sans-serif;font-weight:800;font-size:92px;letter-spacing:10px;color:var(--ghost);line-height:1}
  .sec-title{font-family:"Saira",sans-serif;font-weight:700;font-size:40px;letter-spacing:1px;line-height:1}

  /* tabs */
  .tabs{left:162px;top:969px;width:877px;height:100px;display:flex;border:1px solid #c9d1dd}
  .tab{flex:1;display:flex;align-items:center;justify-content:center;text-align:center;
    font-weight:600;font-size:17px;line-height:25px;border-left:1px solid #c9d1dd}
  .tab:first-child{border-left:none;background:var(--white);color:var(--text-dark);font-weight:500}

  .product-photo{left:112px;top:1140px;width:436px;height:420px;border-radius:10px;
    background:linear-gradient(110deg,#b9b2aa 0%,#8b7e72 35%,#c7b3a6 60%,#e2c8cc 80%,#d9d1c8 100%)}
  .product{left:608px;top:1136px;width:490px}
  .product h3{font-weight:500;font-size:27px;line-height:36px}
  .ticks{list-style:none;margin-top:28px}
  .ticks li{position:relative;padding-left:30px;font-size:16px;line-height:23px;margin-bottom:23px}
  .ticks svg{position:absolute;left:0;top:3px}

  .btn{display:flex;align-items:center;justify-content:center;border-radius:30px;
    background:linear-gradient(90deg,var(--pink),var(--violet));font-weight:600;font-size:18px;letter-spacing:.5px}
  .btn-more{left:604px;top:1663px;width:171px;height:57px}

  /* contact */
  .contact{left:0;top:1808px;width:1200px;height:682px;background:var(--panel)}
  .contact .ghost{color:var(--ghost2)}
  .field{height:80px;border-bottom:1px solid var(--line);font-size:18px;padding:18px 0 0 13px}
  .message{left:166px;top:2178px;width:868px;height:128px;background:var(--field);font-size:18px;padding:18px 13px}
  .btn-submit{left:532px;top:2358px;width:136px;height:57px}

  /* footer */
  .footer{left:0;top:2490px;width:1200px;height:105px;background:var(--page);font-size:17px}
  .copy{left:112px;top:43px}
  .legal{left:338px;top:43px;display:flex;gap:27px}
  .social{right:112px;top:34px;display:flex;gap:9px}
  .social span{width:39px;height:39px;border-radius:50%;background:linear-gradient(135deg,var(--pink),var(--violet))}
</style>
</head>
<body>

<div class="hero" role="img" aria-label="Photo: young man checking his phone while leaning on an electric car that is charging at sunset by the sea"></div>
<svg class="hero-edge" viewBox="0 0 1200 110" aria-hidden="true">
  <path d="M0 50 H1200 V110 H0 Z" fill="#061629"/>
  <path d="M105 50 Q140 100 195 102 Q250 100 290 50 Z" fill="#172a48"/>
  <path d="M930 50 Q950 105 1015 106 Q1090 104 1115 50 Z" fill="#6d6478"/>
</svg>

<div class="abs brand"><span class="brand-dot"></span>mero-kant.de</div>
<nav class="abs nav"><span>Solutions</span><span>Company</span><span>Services</span><span>Career</span><span>Contact</span></nav>

<div class="abs hero-copy">
  <div class="kicker">Just more than loading</div>
  <h1 class="hero-title">Mero-kant is your partner</h1>
  <p class="lead">When loading is not only supposed to be easy, but also when the implementation is to come from a single source</p>
  <p>We offer solutions for private customers, business customers and municipalities who want to get a smart charging solution for e-vehicles quickly, fairly and without having to do anything themselves.</p>
  <p>From advice to installation, commissioning, billing and maintenance, you get everything from a single source with mero-kant. On request, we also rent out the charging technology and take care of direct billing with the user in the commercial sector. For municipalities we offer the free full service and involve the municipalities in the use of the infrastructure.</p>
  <p>Ask us about the solution tailored to your individual needs:</p>
</div>

<div class="abs sec-head" style="top:838px"><div class="ghost">SOLUTIONS</div></div>
<div class="abs sec-head" style="top:884px"><h2 class="sec-title">PRODUCTS</h2></div>

<div class="abs tabs">
  <div class="tab">Wallboxes for<br>single-family homes</div>
  <div class="tab">Property Management<br>/ Parking</div>
  <div class="tab">Municipalities<br>/Communities</div>
  <div class="tab">Tourism/hotels/<br>Holiday appartments</div>
</div>

<div class="abs product-photo" role="img" aria-label="Photo: wallbox charging plug in a car with a woman in the blurred background"></div>

<div class="abs product">
  <h3>Wallboxes for single-family homes</h3>
  <ul class="ticks">
    <li><svg width="17" height="17" viewBox="0 0 17 17"><circle cx="8.5" cy="8.5" r="8.5" fill="var(--tick)"/><path d="M4.6 8.7l2.6 2.6 5-5" stroke="#fff" stroke-width="2" fill="none"/></svg>Analysis of the situation with extensive advice on the possibilities of implementation</li>
    <li><svg width="17" height="17" viewBox="0 0 17 17"><circle cx="8.5" cy="8.5" r="8.5" fill="var(--tick)"/><path d="M4.6 8.7l2.6 2.6 5-5" stroke="#fff" stroke-width="2" fill="none"/></svg>Checking and acceptance of the registration for available funding opportunities</li>
    <li><svg width="17" height="17" viewBox="0 0 17 17"><circle cx="8.5" cy="8.5" r="8.5" fill="var(--tick)"/><path d="M4.6 8.7l2.6 2.6 5-5" stroke="#fff" stroke-width="2" fill="none"/></svg>Selection of smart wallbox solutions, suitable for your vehicle and your needs</li>
    <li><svg width="17" height="17" viewBox="0 0 17 17"><circle cx="8.5" cy="8.5" r="8.5" fill="var(--tick)"/><path d="M4.6 8.7l2.6 2.6 5-5" stroke="#fff" stroke-width="2" fill="none"/></svg>Installation including all necessary materials and activities (breakthroughs, earthworks, etc.)</li>
    <li><svg width="17" height="17" viewBox="0 0 17 17"><circle cx="8.5" cy="8.5" r="8.5" fill="var(--tick)"/><path d="M4.6 8.7l2.6 2.6 5-5" stroke="#fff" stroke-width="2" fill="none"/></svg>Commissioning and instruction in charging technology</li>
    <li><svg width="17" height="17" viewBox="0 0 17 17"><circle cx="8.5" cy="8.5" r="8.5" fill="var(--tick)"/><path d="M4.6 8.7l2.6 2.6 5-5" stroke="#fff" stroke-width="2" fill="none"/></svg>Annual technical maintenance according to DGUV3</li>
    <li><svg width="17" height="17" viewBox="0 0 17 17"><circle cx="8.5" cy="8.5" r="8.5" fill="var(--tick)"/><path d="M4.6 8.7l2.6 2.6 5-5" stroke="#fff" stroke-width="2" fill="none"/></svg>Repair service, taking into account the applicable warranty claims</li>
  </ul>
</div>
<div class="abs btn btn-more">READ MORE</div>

<section class="abs contact">
  <div class="abs sec-head" style="top:68px"><div class="ghost">CONTACT US</div></div>
  <div class="abs sec-head" style="top:112px"><h2 class="sec-title">REQUEST FOR INFORMATION</h2></div>
  <div class="abs field" style="left:166px;top:169px;width:422px">First Name</div>
  <div class="abs field" style="left:612px;top:169px;width:422px">Last Name</div>
  <div class="abs field" style="left:166px;top:255px;width:422px">Email</div>
  <div class="abs field" style="left:612px;top:255px;width:422px">Address</div>
</section>
<div class="abs message">Message</div>
<div class="abs btn btn-submit">SUBMIT</div>

<footer class="abs footer">
  <div class="abs copy">©mero-kant GmbH</div>
  <div class="abs legal"><span>AGB</span><span>Data protection</span><span>Imprint</span><span>Contact</span><span>Career</span><span>FAQs</span></div>
  <div class="abs social"><span></span><span></span><span></span></div>
</footer>

</body>
</html>
```